Corvid Lens Studio Business Card Design

I need a business card designed for a photography business based in Perth, Western Australia called Corvid Lens Studio.

We specialise in wedding, event photography and portrait photography.

The business card must borrow the style of the attached logo.

The hex codes for the colours in the logo are:
#ED1D85 - Pink
#89C23E - Green
#37282F - Black

The name on the card will be:
Name: Tobiah
Phone: 0417395268
Website: www.corvidlensstudio.com.au
Facebook: corvidlensstudio

I am open and happy to accept creative concepts.

Industry/Entity Type

Business

```html
<!DOCTYPE html>
<html lang="en">
<head>
<meta charset="utf-8">
<title>Corvid Lens Studio — Business Card</title>
<link rel="stylesheet" href="https://fonts.googleapis.com/css2?family=Questrial&display=swap">
<style>
  :root {
    --pink: #ED1D85;
    --green: #89C23E;
    --ink: #37282F;
    --paper: #FFFFFF;
    --backdrop: #EEEEEF;
    --card-shadow: rgba(55, 40, 47, 0.12);
  }
  * { margin: 0; padding: 0; box-sizing: border-box; }
  html, body {
    width: 1200px;
    height: 720px;
    overflow: hidden;
    background: var(--backdrop);
    font-family: "Questrial", "Century Gothic", sans-serif;
  }
  .canvas {
    position: relative;
    width: 1200px;
    height: 720px;
    display: flex;
    align-items: center;
    justify-content: center;
    gap: 48px;
  }
  .card {
    position: relative;
    width: 520px;
    height: 300px;
    background: var(--paper);
    box-shadow: 0 2px 10px var(--card-shadow);
    overflow: hidden;
  }

  /* Front */
  .card--front {
    display: flex;
    flex-direction: column;
    align-items: center;
    justify-content: center;
    gap: 22px;
  }
  .brand-dot {
    width: 34px;
    height: 34px;
    border-radius: 50%;
    background: var(--pink);
  }
  .brand-name {
    font-size: 13px;
    letter-spacing: 0.55em;
    text-transform: uppercase;
    color: var(--ink);
    padding-left: 0.55em;
  }

  /* Back */
  .card--back .mark-circle {
    position: absolute;
    left: -110px;
    top: 40px;
    width: 220px;
    height: 220px;
  }
  .identity {
    position: absolute;
    right: 34px;
    top: 34px;
    text-align: right;
  }
  .identity__name {
    font-size: 50px;
    line-height: 1;
    color: var(--ink);
    letter-spacing: 0.01em;
  }
  .identity__role {
    font-size: 16px;
    color: var(--pink);
    margin-top: -4px;
  }
  .contact {
    position: absolute;
    right: 34px;
    top: 146px;
    list-style: none;
    text-align: right;
    color: var(--green);
    font-size: 14px;
    line-height: 1.55;
    letter-spacing: 0.02em;
  }
</style>
</head>
<body>
  <main class="canvas">
    <section class="card card--front" aria-label="Business card front">
      <span class="brand-dot" aria-hidden="true"></span>
      <p class="brand-name">Corvid Lens Studio</p>
    </section>

    <section class="card card--back" aria-label="Business card back">
      <svg class="mark-circle" viewBox="0 0 220 220" aria-hidden="true">
        <circle cx="110" cy="110" r="110" fill="var(--pink)"/>
      </svg>
      <div class="identity">
        <h1 class="identity__name">Tobiah</h1>
        <p class="identity__role">Photographer</p>
      </div>
      <ul class="contact">
        <li class="contact__phone">041 739 5268</li>
        <li class="contact__web">www.corvidlensstudio.com.au</li>
        <li class="contact__social">Facebook: corvidlensstudio</li>
      </ul>
    </section>
  </main>
</body>
</html>
```